App Design for quiz app (casual gaming app)

We need an design & logo for our quiz app. Its a simple quiz app, where you pick up a category, answer three questions out of this category. After this an opponent is assigned to your game, and has to answer the same three questions. After this first round is finished, it's the opponents turn to choose a new category and answer three questions out of this category. Now it's your turn to answer the same three questions. With this done, the 2nd round is finished. One game has seven rounds.
Please find attached the balsamiq project. For all of you, do not have balsamiq, please find also the mockups as pdf.
Final delivery should be psd files
Target Market(s)
Casual Games

```html
<!DOCTYPE html>
<html lang="en">
<head>
<meta charset="utf-8">
<title>Quiz App Screens</title>
<link href="https://fonts.googleapis.com/css2?family=Roboto:wght@300;400;500;700&display=swap" rel="stylesheet">
<style>
:root{
  --green:#4d8d10;
  --green-text:#5a9a1a;
  --bg:#f4f4f4;
  --footer:#e9e9e9;
  --line:#dddddd;
  --muted:#777777;
  --label:#8a8a8a;
  --blue:#5372b8;
  --teal:#3fcfcf;
  --gold:#dfac1c;
  --soft-green:#9cc68a;
  --dot-green:#9ccf7a;
  --dot-yellow:#f2c12e;
  --dot-gray:#dcdcdc;
  --tile-green:#a6cf94;
  --tile-blue:#8fb9ef;
  --tile-pink:#c37ba2;
  --tile-yellow:#f0c030;
  --black:#000000;
  --menu-dark:#2b2b2b;
}
*{box-sizing:border-box;margin:0;padding:0}
html,body{width:1200px;height:960px;overflow:hidden;background:#ffffff;font-family:"Roboto",sans-serif}
.stage{position:relative;width:1500px;height:1200px;transform:scale(.8);transform-origin:0 0}
.screen{position:absolute;width:256px;background:var(--bg);box-shadow:0 2px 5px rgba(0,0,0,.18);overflow:hidden}
.abs{position:absolute}
.status{position:absolute;left:0;top:0;width:100%;height:16px;background:var(--green);color:#fff;font-size:8px;display:flex;align-items:center;justify-content:space-between;padding:0 4px}
.status .bat{display:inline-block;width:18px;height:7px;background:#fff;border-radius:1px;margin-left:3px;vertical-align:middle}
.appbar{position:absolute;left:0;top:16px;width:100%;height:40px;background:var(--green);color:#fff;font-size:14px;font-weight:300;display:flex;align-items:center;justify-content:center}
.appbar .back,.appbar .menu,.appbar .act{position:absolute;top:12px}
.appbar .back{left:10px}
.appbar .menu{left:12px}
.appbar .act{right:12px}
.screen-label{position:absolute;width:256px;text-align:center;font-size:24px;font-weight:300;color:var(--label)}
.logo-word{position:absolute;width:100%;text-align:center;font-size:22px;color:var(--green-text)}
.divider{position:absolute;left:14px;right:14px;height:1px;background:var(--line)}
.divider span{position:absolute;left:50%;top:-6px;transform:translateX(-50%);background:var(--bg);padding:0 6px;font-size:8px;font-weight:700;color:#333;white-space:nowrap}
.or{position:absolute;left:50%;width:16px;height:16px;margin-left:-8px;border:1px solid var(--line);border-radius:50%;background:var(--bg);font-size:5px;font-weight:700;color:var(--green-text);display:flex;align-items:center;justify-content:center}
.field{position:absolute;left:14px;width:228px;height:28px;background:#fff;border:1px solid #e4e4e4;font-size:8px;color:#777;display:flex;align-items:center;padding-left:38px}
.field svg{position:absolute;left:12px;top:7px}
.field.pass{font-size:12px;letter-spacing:1px;color:#555}
.btn{position:absolute;left:14px;width:228px;height:29px;color:#fff;font-size:11px;display:flex;align-items:center;justify-content:center}
.btn.green{background:var(--green)}
.btn.blue{background:var(--blue)}
.btn.white{background:#fff;color:var(--green-text);border:1px solid #ddd}
.btn .mark{position:absolute;left:14px;top:4px;width:20px;height:20px;border-radius:50%;background:#fff}
.small{position:absolute;width:100%;text-align:center;font-size:8px;color:var(--muted)}
.footer{position:absolute;left:0;width:100%;bottom:0;background:var(--footer)}
.photo{position:absolute;border-radius:50%;background:radial-gradient(circle at 50% 40%,#e2b596 0%,#b07650 45%,#5b3421 100%)}
.name{position:absolute;width:100%;text-align:center;font-size:11px;color:var(--green-text)}
.card{position:absolute;left:10px;width:236px;height:60px;background:#ececec;box-shadow:0 1px 2px rgba(0,0,0,.08)}
.card .photo{left:7px;top:7px;width:46px;height:46px}
.card .who{position:absolute;left:64px;top:12px;font-size:8px;color:var(--green-text)}
.card .meta{position:absolute;left:64px;font-size:7px;color:#888}
.card .state{position:absolute;right:6px;top:12px;font-size:8px;color:#888}
.card .pill{position:absolute;right:6px;top:36px;background:var(--green);color:#fff;font-size:7px;padding:2px 5px;border-radius:8px}
.menu-panel{position:absolute;left:0;top:0;width:200px;height:100%;background:var(--black)}
.menu-item{position:absolute;left:0;width:200px;height:43px;border-top:1px solid #262626;color:#fff;font-size:10px;display:flex;align-items:center;padding-left:40px}
.menu-item.active{background:var(--menu-dark);color:var(--green-text)}
.menu-item svg.ico{position:absolute;left:13px;top:14px}
.menu-item .chev{position:absolute;right:10px;top:15px}
.lead{position:absolute;width:100%;text-align:center;font-size:10px;color:var(--green-text);padding:0 20px;line-height:12px}
.pick{position:absolute;left:17px;width:222px;height:28px;color:#fff;font-size:10px;display:flex;align-items:center;justify-content:center}
.pick .mark{position:absolute;left:13px;top:4px;width:20px;height:20px;border-radius:50%;border:2px solid #fff}
.tile{position:absolute;width:117px;height:117px;color:#fff;text-align:center}
.tile b{display:block;font-size:26px;font-weight:400;margin-top:24px}
.tile span{display:block;font-size:10px;margin-top:10px}
.qbadge{position:absolute;left:103px;top:282px;width:48px;height:48px;border-radius:50%;background:var(--green);border:3px solid #fff;color:#fff;font-size:28px;font-weight:300;display:flex;align-items:center;justify-content:center}
.qcard{position:absolute;left:16px;top:73px;width:224px;height:92px;background:#fff;border:1px solid #e6e6e6;padding:10px 10px 0 28px;font-size:9.5px;color:#444;line-height:12.5px}
.qcard b{position:absolute;left:9px;top:10px;color:#d22;font-size:9px}
.answer{position:absolute;left:16px;width:223px;height:28px;color:#fff;font-size:9.5px;display:flex;align-items:center;justify-content:center}
.answer i{position:absolute;left:12px;top:5px;width:18px;height:18px;border-radius:50%;background:#fff;font-style:normal;font-size:7px;color:#e7a21a;display:flex;align-items:center;justify-content:center}
.vs{position:absolute;left:0;width:100%;text-align:center;font-size:20px;font-weight:300;font-style:italic;color:#888}
.score{position:absolute;left:100px;top:116px;width:56px;display:flex;justify-content:space-between;align-items:center;font-size:12px;color:#999}
.score span{background:#eaeaea;width:22px;height:22px;display:flex;align-items:center;justify-content:center}
.pname{position:absolute;width:90px;text-align:center;font-size:10px;color:var(--green-text)}
.round{position:absolute;left:11px;width:234px;height:60px;background:#ececec;box-shadow:0 1px 2px rgba(0,0,0,.08)}
.round .rt{position:absolute;width:100%;top:6px;text-align:center;font-size:8px;color:var(--green-text)}
.round .rc{position:absolute;width:100%;top:18px;text-align:center;font-size:7px;color:#999}
.round .br{position:absolute;top:28px;height:6px;border:1px solid #d0d0d0;border-bottom:none}
.dot{position:absolute;top:36px;width:14px;height:14px;border-radius:50%}
.g{background:var(--dot-green)} .y{background:var(--dot-yellow)} .n{background:var(--dot-gray)}
</style>
</head>
<body>
<div class="stage">

<!-- Log In -->
<section class="screen login" style="left:34px;top:15px;height:454px">
  <div class="status"><span>●●●○○ Nimbus ◠</span><span>4:21 PM</span><span>100%<i class="bat"></i></span></div>
  <div class="appbar">Log In</div>
  <div class="logo-word" style="top:86px">Logo Here</div>
  <div class="divider" style="top:143px"><span>Welcome to Quiz Game</span></div>
  <div class="field" style="top:166px"><svg width="14" height="14" viewBox="0 0 14 14"><circle cx="7" cy="7" r="6" fill="none" stroke="#999"/><circle cx="7" cy="5.5" r="2" fill="none" stroke="#999"/></svg>User Name</div>
  <div class="field pass" style="top:201px"><svg width="14" height="14" viewBox="0 0 14 14"><rect x="2" y="6" width="10" height="7" fill="none" stroke="#999"/><path d="M4 6V4a3 3 0 0 1 6 0v2" fill="none" stroke="#999"/></svg>••••••••</div>
  <div class="btn green" style="top:250px">Login</div>
  <div class="small" style="top:288px">Forget your password?</div>
  <div class="divider" style="top:323px"></div><div class="or" style="top:315px">OR</div>
  <div class="btn blue" style="top:350px"><i class="mark"></i>Login with Circlebook</div>
  <div class="footer" style="height:61px">
    <div class="small" style="top:6px">Do not have account yet?</div>
    <div class="btn white" style="top:22px">Register an Account</div>
  </div>
</section>
<div class="screen-label" style="left:34px;top:500px">Log In</div>

<!-- Sign Up -->
<section class="screen signup" style="left:329px;top:15px;height:454px">
  <div class="status"><span>●●●○○ Nimbus ◠</span><span>4:21 PM</span><span>100%<i class="bat"></i></span></div>
  <div class="appbar"><svg class="back" width="10" height="16" viewBox="0 0 10 16"><path d="M8 2 2 8l6 6" fill="none" stroke="#fff" stroke-width="1.5"/></svg>Signup</div>
  <div class="logo-word" style="top:67px">Logo Here</div>
  <div class="field" style="top:114px"><svg width="14" height="14" viewBox="0 0 14 14"><circle cx="7" cy="7" r="6" fill="none" stroke="#999"/><circle cx="7" cy="5.5" r="2" fill="none" stroke="#999"/></svg>First Name</div>
  <div class="field" style="top:147px"><svg width="14" height="14" viewBox="0 0 14 14"><circle cx="7" cy="7" r="6" fill="none" stroke="#999"/><circle cx="7" cy="5.5" r="2" fill="none" stroke="#999"/></svg>Last Name</div>
  <div class="field" style="top:180px"><svg width="14" height="14" viewBox="0 0 14 14"><circle cx="7" cy="7" r="6" fill="none" stroke="#999"/><circle cx="7" cy="5.5" r="2" fill="none" stroke="#999"/></svg>User Name</div>
  <div class="field" style="top:213px"><svg width="14" height="14" viewBox="0 0 14 14"><rect x="2" y="6" width="10" height="7" fill="none" stroke="#999"/><path d="M4 6V4a3 3 0 0 1 6 0v2" fill="none" stroke="#999"/></svg>Create Password</div>
  <div class="field" style="top:246px"><svg width="14" height="14" viewBox="0 0 14 14"><rect x="2" y="6" width="10" height="7" fill="none" stroke="#999"/><path d="M4 6V4a3 3 0 0 1 6 0v2" fill="none" stroke="#999"/></svg>Confirm Password</div>
  <div class="btn green" style="top:301px">Signup</div>
  <div class="divider" style="top:362px"></div><div class="or" style="top:354px">OR</div>
  <div class="footer" style="height:69px">
    <div class="small" style="top:12px">Have an account?</div>
    <div class="btn white" style="top:30px">Login an Account</div>
  </div>
</section>
<div class="screen-label" style="left:329px;top:500px">Sign Up</div>

<!-- Create New Game -->
<section class="screen games" style="left:623px;top:15px;height:454px">
  <div class="status"><span>●●●○○ Nimbus ◠</span><span>4:21 PM</span><span>100%<i class="bat"></i></span></div>
  <div class="appbar"><svg class="menu" width="16" height="12" viewBox="0 0 16 12"><path d="M0 1h16M0 6h16M0 11h16" stroke="#fff" stroke-width="1.5"/></svg>Create New Game<svg class="act" width="14" height="14" viewBox="0 0 14 14"><circle cx="7" cy="7" r="7" fill="#9cc68a"/><path d="M7 3v8M3 7h8" stroke="#fff" stroke-width="1.5"/></svg></div>
  <div class="photo" role="img" aria-label="Player portrait photo" style="left:99px;top:75px;width:58px;height:58px"></div>
  <div class="name" style="top:140px">Maya Brooks</div>
  <div class="card" style="top:180px"><div class="photo" role="img" aria-label="Opponent portrait photo"></div><div class="who">Leo Grant</div><div class="meta" style="top:26px">Round 2</div><div class="meta" style="top:38px">3 : 7</div><div class="state">My Turn</div><div class="pill">Opponent</div></div>
  <div class="card" style="top:250px"><div class="photo" role="img" aria-label="Opponent portrait photo"></div><div class="who">Nina Park</div><div class="meta" style="top:26px">Round 2</div><div class="meta" style="top:38px">3 : 7</div><div class="state">Waiting For Player</div><div class="pill">Opponent</div></div>
  <div class="card" style="top:320px"><div class="photo" role="img" aria-label="Opponent portrait photo"></div><div class="who">Owen Hale</div><div class="meta" style="top:26px">Round 2</div><div class="meta" style="top:38px">3 : 7</div><div class="state">Finished Game</div><div class="pill">Opponent</div></div>
  <div class="btn green" style="top:409px;left:12px;width:232px">Create New Game</div>
</section>
<div class="screen-label" style="left:623px;top:500px">Create New Game</div>

<!-- Side Menu -->
<section class="screen side-menu" style="left:918px;top:15px;height:454px">
  <div class="appbar" style="top:0;height:56px"><svg class="act" style="top:30px" width="16" height="12" viewBox="0 0 16 12"><path d="M0 1h16M0 6h16M0 11h16" stroke="#fff" stroke-width="1.5"/></svg></div>
  <div class="photo" role="img" aria-label="Opponent portrait photo" style="left:218px;top:188px;width:40px;height:44px"></div>
  <div class="photo" role="img" aria-label="Opponent portrait photo" style="left:218px;top:258px;width:40px;height:44px"></div>
  <div class="photo" role="img" aria-label="Opponent portrait photo" style="left:218px;top:328px;width:40px;height:44px"></div>
  <div class="abs" style="left:212px;top:409px;width:44px;height:29px;background:var(--green)"></div>
  <div class="menu-panel">
    <div class="status" style="background:var(--black)"><span>●●●○○ Nimbus ◠</span><span>4:21 PM</span><span></span></div>
    <div class="photo" role="img" aria-label="Player portrait photo" style="left:69px;top:46px;width:60px;height:60px"></div>
    <div class="name" style="top:113px">Maya Brooks</div>
    <div class="menu-item" style="top:153px"><svg class="ico" width="14" height="14" viewBox="0 0 14 14"><ellipse cx="7" cy="7" rx="6.5" ry="4" fill="#fff"/><circle cx="7" cy="7" r="2" fill="#000"/></svg>Overview<svg class="chev" width="6" height="10"><path d="M1 1l4 4-4 4" fill="none" stroke="#444"/></svg></div>
    <div class="menu-item active" style="top:196px"><svg class="ico" width="14" height="14" viewBox="0 0 14 14" fill="#5a9a1a"><circle cx="4" cy="4" r="2.5"/><circle cx="10" cy="4" r="2.5"/><circle cx="7" cy="10" r="2.5"/></svg>My Groups<svg class="chev" width="6" height="10"><path d="M1 1l4 4-4 4" fill="none" stroke="#5a9a1a"/></svg></div>
    <div class="menu-item" style="top:239px"><svg class="ico" width="14" height="14" viewBox="0 0 14 14" fill="#fff"><circle cx="5" cy="4" r="3"/><path d="M0 13a5 5 0 0 1 10 0z"/><circle cx="10.5" cy="4.5" r="2.5"/></svg>Invite Friends<svg class="chev" width="6" height="10"><path d="M1 1l4 4-4 4" fill="none" stroke="#444"/></svg></div>
    <div class="menu-item" style="top:282px"><svg class="ico" width="14" height="14" viewBox="0 0 14 14" fill="#fff"><path d="M1 1v12h12" fill="none" stroke="#fff"/><rect x="3" y="7" width="2" height="5"/><rect x="6" y="4" width="2" height="8"/><rect x="9" y="6" width="2" height="6"/></svg>Stats<svg class="chev" width="6" height="10"><path d="M1 1l4 4-4 4" fill="none" stroke="#444"/></svg></div>
    <div class="menu-item" style="top:325px"><svg class="ico" width="14" height="14" viewBox="0 0 14 14"><circle cx="7" cy="7" r="6" fill="#fff"/><circle cx="7" cy="7" r="2.5" fill="#000"/></svg>Help<svg class="chev" width="6" height="10"><path d="M1 1l4 4-4 4" fill="none" stroke="#444"/></svg></div>
    <div class="menu-item" style="top:368px"><svg class="ico" width="14" height="14" viewBox="0 0 14 14"><path d="M3 5v5a4 4 0 0 0 8 0V4M5 2v6M7 1v7M9 2v6" fill="none" stroke="#fff" stroke-width="1.2"/></svg>Imprint<svg class="chev" width="6" height="10"><path d="M1 1l4 4-4 4" fill="none" stroke="#444"/></svg></div>
    <div class="menu-item" style="top:411px"><svg class="ico" width="14" height="14" viewBox="0 0 14 14"><path d="M6 2H2v10h10V8M8 1h5v5M13 1 6 8" fill="none" stroke="#fff" stroke-width="1.3"/></svg>Signout</div>
  </div>
</section>
<div class="screen-label" style="left:918px;top:500px">Side Menu</div>

<!-- Create New Game: opponent source -->
<section class="screen new-game" style="left:1212px;top:15px;height:454px">
  <div class="status"><span>●●●○○ Nimbus ◠</span><span>4:21 PM</span><span>100%<i class="bat"></i></span></div>
  <div class="appbar"><svg class="back" width="10" height="16" viewBox="0 0 10 16"><path d="M8 2 2 8l6 6" fill="none" stroke="#fff" stroke-width="1.5"/></svg>Create New Game</div>
  <div class="lead" style="top:72px">Lorem Ipsum is simply dummy text.</div>
  <div class="divider" style="top:106px"><span style="font-weight:400;color:#777">Welcome to New Game</span></div>
  <div class="lead" style="top:159px">Lorem Ipsum is simply dummy text of the printing and typesetting industry.</div>
  <div class="pick" style="top:216px;background:var(--soft-green)"><i class="mark" style="background:#fff"></i>Search for Players</div>
  <div class="pick" style="top:256px;background:var(--blue)"><i class="mark" style="background:#fff"></i>Circlebook Friends</div>
  <div class="pick" style="top:296px;background:var(--gold)"><i class="mark"></i>Random Players</div>
</section>
<div class="screen-label" style="left:1212px;top:500px">Create New Game</div>

<!-- Question Category -->
<section class="screen category" style="left:34px;top:567px;height:454px">
  <div class="status"><span>●●●○○ Nimbus ◠</span><span>4:21 PM</span><span>100%<i class="bat"></i></span></div>
  <div class="appbar"><svg class="back" width="10" height="16" viewBox="0 0 10 16"><path d="M8 2 2 8l6 6" fill="none" stroke="#fff" stroke-width="1.5"/></svg>Question Category</div>
  <div class="photo" role="img" aria-label="Player portrait photo" style="left:93px;top:76px;width:70px;height:70px"></div>
  <div class="name" style="top:151px;font-size:12px;font-weight:500">Maya Brooks</div>
  <div class="tile" style="left:10px;top:189px;background:var(--tile-green)"><b>1</b><span>Question Category</span></div>
  <div class="tile" style="left:129px;top:189px;background:var(--tile-blue)"><b>2</b><span>Question Category</span></div>
  <div class="tile" style="left:10px;top:310px;background:var(--tile-pink)"><b>3</b><span>Question Category</span></div>
  <div class="tile" style="left:129px;top:310px;background:var(--tile-yellow)"><b>4</b><span>Question Category</span></div>
  <div class="qbadge">?</div>
</section>
<div class="screen-label" style="left:34px;top:1058px">Question Category</div>

<!-- Question -->
<section class="screen question" style="left:329px;top:567px;height:454px">
  <div class="status"><span>●●●○○ Nimbus ◠</span><span>4:21 PM</span><span>100%<i class="bat"></i></span></div>
  <div class="appbar"><svg class="back" width="10" height="16" viewBox="0 0 10 16"><path d="M8 2 2 8l6 6" fill="none" stroke="#fff" stroke-width="1.5"/></svg>Question<svg class="act" width="14" height="14" viewBox="0 0 14 14"><circle cx="7" cy="7" r="7" fill="#9cc68a"/><path d="M10 7a3 3 0 1 1-1-2.2" fill="none" stroke="#fff" stroke-width="1.3"/></svg></div>
  <div class="qcard"><b>Q :</b>Lorem Ipsum has been the industry's standard dummy text ever since the 1500s, when an unknown printer took a galley of type and scrambled it to make a type specimen book?</div>
  <div class="answer" style="top:204px;background:var(--soft-green)"><i>A:</i>Answer - 1</div>
  <div class="answer" style="top:244px;background:var(--blue)"><i>A:</i>Answer - 2</div>
  <div class="answer" style="top:284px;background:var(--teal)"><i>A:</i>Answer - 3</div>
  <div class="answer" style="top:324px;background:var(--gold)"><i>A:</i>Answer - 4</div>
</section>
<div class="screen-label" style="left:329px;top:1058px">Question</div>

<!-- My Turn Overview -->
<section class="screen overview" style="left:623px;top:567px;height:580px">
  <div class="status"><span>●●●○○ Nimbus ◠</span><span>4:21 PM</span><span>100%<i class="bat"></i></span></div>
  <div class="appbar"><svg class="back" width="10" height="16" viewBox="0 0 10 16"><path d="M8 2 2 8l6 6" fill="none" stroke="#fff" stroke-width="1.5"/></svg>My Turn Overview</div>
  <div class="photo" role="img" aria-label="Player portrait photo" style="left:18px;top:70px;width:52px;height:52px"></div>
  <div class="photo" role="img" aria-label="Opponent portrait photo" style="left:185px;top:70px;width:52px;height:52px"></div>
  <div class="vs" style="top:68px">Vs</div>
  <div class="score"><span>15</span>:<span>13</span></div>
  <div class="pname" style="left:0;top:128px">Leo Grant</div><div class="pname" style="left:166px;top:128px">Maya Brooks</div>
  <div class="round" style="top:178px"><div class="rt">Round 01</div><div class="rc">Category</div><i class="br" style="left:26px;width:40px"></i><i class="br" style="left:183px;width:40px"></i><i class="dot g" style="left:12px"></i><i class="dot g" style="left:32px"></i><i class="dot y" style="left:52px"></i><i class="dot g" style="left:169px"></i><i class="dot y" style="left:189px"></i><i class="dot y" style="left:209px"></i></div>
  <div class="round" style="top:246px"><div class="rt">Round 02</div><div class="rc">Category</div><i class="br" style="left:26px;width:40px"></i><i class="br" style="left:183px;width:40px"></i><i class="dot n" style="left:12px"></i><i class="dot n" style="left:32px"></i><i class="dot n" style="left:52px"></i><i class="dot g" style="left:169px"></i><i class="dot g" style="left:189px"></i><i class="dot y" style="left:209px"></i></div>
  <div class="round" style="top:314px"><div class="rt">Round 03</div><div class="rc">Category</div><i class="br" style="left:26px;width:40px"></i><i class="br" style="left:183px;width:40px"></i><i class="dot n" style="left:12px"></i><i class="dot n" style="left:32px"></i><i class="dot n" style="left:52px"></i><i class="dot n" style="left:169px"></i><i class="dot n" style="left:189px"></i><i class="dot n" style="left:209px"></i></div>
  <div class="round" style="top:382px"><div class="rt">Round 04</div><div class="rc">Category</div><i class="br" style="left:26px;width:40px"></i><i class="br" style="left:183px;width:40px"></i><i class="dot n" style="left:12px"></i><i class="dot n" style="left:32px"></i><i class="dot n" style="left:52px"></i><i class="dot n" style="left:169px"></i><i class="dot n" style="left:189px"></i><i class="dot n" style="left:209px"></i></div>
  <div class="round" style="top:450px"><div class="rt">Round 05</div><div class="rc">Category</div><i class="br" style="left:26px;width:40px"></i><i class="br" style="left:183px;width:40px"></i><i class="dot n" style="left:12px"></i><i class="dot n" style="left:32px"></i><i class="dot n" style="left:52px"></i><i class="dot n" style="left:169px"></i><i class="dot n" style="left:189px"></i><i class="dot n" style="left:209px"></i></div>
  <div class="btn green" style="top:537px;left:12px;width:232px">Resume Game</div>
</section>
<div class="screen-label" style="left:623px;top:1160px">My Turn Overview</div>

<!-- Waiting Overview -->
<section class="screen overview" style="left:918px;top:567px;height:580px">
  <div class="status"><span>●●●○○ Nimbus ◠</span><span>4:21 PM</span><span>100%<i class="bat"></i></span></div>
  <div class="appbar"><svg class="back" width="10" height="16" viewBox="0 0 10 16"><path d="M8 2 2 8l6 6" fill="none" stroke="#fff" stroke-width="1.5"/></svg>Waiting Overview</div>
  <div class="photo" role="img" aria-label="Player portrait photo" style="left:18px;top:70px;width:52px;height:52px"></div>
  <div class="photo" role="img" aria-label="Opponent portrait photo" style="left:185px;top:70px;width:52px;height:52px"></div>
  <div class="vs" style="top:68px">Vs</div>
  <div class="score"><span>15</span>:<span>13</span></div>
  <div class="pname" style="left:0;top:128px">Leo Grant</div><div class="pname" style="left:166px;top:128px">Maya Brooks</div>
  <div class="round" style="top:178px"><div class="rt">Round 01</div><div class="rc">Category</div><i class="br" style="left:26px;width:40px"></i><i class="br" style="left:183px;width:40px"></i><i class="dot g" style="left:12px"></i><i class="dot g" style="left:32px"></i><i class="dot y" style="left:52px"></i><i class="dot g" style="left:169px"></i><i class="dot y" style="left:189px"></i><i class="dot y" style="left:209px"></i></div>
  <div class="round" style="top:246px"><div class="rt">Round 02</div><div class="rc">Category</div><i class="br" style="left:26px;width:40px"></i><i class="br" style="left:183px;width:40px"></i><i class="dot n" style="left:12px"></i><i class="dot n" style="left:32px"></i><i class="dot n" style="left:52px"></i><i class="dot g" style="left:169px"></i><i class="dot g" style="left:189px"></i><i class="dot y" style="left:209px"></i></div>
  <div class="round" style="top:314px"><div class="rt">Round 03</div><div class="rc">Category</div><i class="br" style="left:26px;width:40px"></i><i class="br" style="left:183px;width:40px"></i><i class="dot n" style="left:12px"></i><i class="dot n" style="left:32px"></i><i class="dot n" style="left:52px"></i><i class="dot n" style="left:169px"></i><i class="dot n" style="left:189px"></i><i class="dot n" style="left:209px"></i></div>
  <div class="round" style="top:382px"><div class="rt">Round 04</div><div class="rc">Category</div><i class="br" style="left:26px;width:40px"></i><i class="br" style="left:183px;width:40px"></i><i class="dot n" style="left:12px"></i><i class="dot n" style="left:32px"></i><i class="dot n" style="left:52px"></i><i class="dot n" style="left:169px"></i><i class="dot n" style="left:189px"></i><i class="dot n" style="left:209px"></i></div>
  <div class="round" style="top:450px"><div class="rt">Round 05</div><div class="rc">Category</div><i class="br" style="left:26px;width:40px"></i><i class="br" style="left:183px;width:40px"></i><i class="dot n" style="left:12px"></i><i class="dot n" style="left:32px"></i><i class="dot n" style="left:52px"></i><i class="dot n" style="left:169px"></i><i class="dot n" style="left:189px"></i><i class="dot n" style="left:209px"></i></div>
  <div class="btn" style="top:537px;left:12px;width:232px;background:var(--gold)">Waiting</div>
</section>
<div class="screen-label" style="left:918px;top:1160px">Waiting Overview</div>

<!-- Finished Overview -->
<section class="screen overview" style="left:1212px;top:567px;height:530px">
  <div class="status"><span>●●●○○ Nimbus ◠</span><span>4:21 PM</span><span>100%<i class="bat"></i></span></div>
  <div class="appbar"><svg class="back" width="10" height="16" viewBox="0 0 10 16"><path d="M8 2 2 8l6 6" fill="none" stroke="#fff" stroke-width="1.5"/></svg>Finished Overview</div>
  <div class="photo" role="img" aria-label="Player portrait photo" style="left:18px;top:70px;width:52px;height:52px"></div>
  <div class="photo" role="img" aria-label="Opponent portrait photo" style="left:185px;top:70px;width:52px;height:52px"></div>
  <div class="vs" style="top:68px">Vs</div>
  <div class="score"><span>15</span>:<span>13</span></div>
  <div class="pname" style="left:0;top:128px">Leo Grant</div><div class="pname" style="left:166px;top:128px">Maya Brooks</div>
  <div class="round" style="top:178px"><div class="rt">Round 01</div><div class="rc">Category</div><i class="br" style="left:26px;width:40px"></i><i class="br" style="left:183px;width:40px"></i><i class="dot g" style="left:12px"></i><i class="dot g" style="left:32px"></i><i class="dot y" style="left:52px"></i><i class="dot g" style="left:169px"></i><i class="dot y" style="left:189px"></i><i class="dot y" style="left:209px"></i></div>
  <div class="round" style="top:246px"><div class="rt">Round 02</div><div class="rc">Category</div><i class="br" style="left:26px;width:40px"></i><i class="br" style="left:183px;width:40px"></i><i class="dot g" style="left:12px"></i><i class="dot g" style="left:32px"></i><i class="dot y" style="left:52px"></i><i class="dot g" style="left:169px"></i><i class="dot g" style="left:189px"></i><i class="dot y" style="left:209px"></i></div>
  <div class="round" style="top:314px"><div class="rt">Round 03</div><div class="rc">Category</div><i class="br" style="left:26px;width:40px"></i><i class="br" style="left:183px;width:40px"></i><i class="dot g" style="left:12px"></i><i class="dot y" style="left:32px"></i><i class="dot g" style="left:52px"></i><i class="dot y" style="left:169px"></i><i class="dot g" style="left:189px"></i><i class="dot g" style="left:209px"></i></div>
  <div class="round" style="top:382px"><div class="rt">Round 04</div><div class="rc">Category</div><i class="br" style="left:26px;width:40px"></i><i class="br" style="left:183px;width:40px"></i><i class="dot y" style="left:12px"></i><i class="dot y" style="left:32px"></i><i class="dot y" style="left:52px"></i><i class="dot y" style="left:169px"></i><i class="dot y" style="left:189px"></i><i class="dot y" style="left:209px"></i></div>
  <div class="round" style="top:450px"><div class="rt">Round 05</div><div class="rc">Category</div><i class="br" style="left:26px;width:40px"></i><i class="br" style="left:183px;width:40px"></i><i class="dot g" style="left:12px"></i><i class="dot y" style="left:32px"></i><i class="dot g" style="left:52px"></i><i class="dot g" style="left:169px"></i><i class="dot g" style="left:189px"></i><i class="dot g" style="left:209px"></i></div>
</section>
<div class="screen-label" style="left:1212px;top:1130px">Finished Overview</div>

</div>
</body>
</html>
```